HARLOWE CONSERVATORY SAXOPHONE SENIOR RECITAL

I need a poster design for my senior saxophone recital. The title of it is "Quill: a Voyage beneath the Edge of Tone". My concept is completely contrasting to the idea of a typical university recital. I'm so put off by the idea of "clap..clap..{play some music}..clap..clap..repeat". My recital is all based off of sound. The music I selected is all very modern (i.e Brem Ostrakel 'Warm from the First Pour' for Saxophone and Coffee Machine). I've included the Chatterbox link so you can see the picture I have in the background. I like the idea of minimal black and white photography. Also, I would like the time / date / location / etc. all included on it. Let your imaginations run wild! It's art for an artist!
https://www.chatterbox-example.net/events/412093857716230/
Target Market(s)
University Students around the Harlowe Conservatory and locals around the art district of South Beach, FL.
Industry/Entity Type
University
Look and feel

```html
<!DOCTYPE html>
<html lang="en">
<head>
<meta charset="utf-8">
<title>Quill: a Voyage beneath the Edge of Tone</title>
<link rel="stylesheet" href="https://fonts.googleapis.com/css2?family=Oswald:wght@300;400;500&family=Raleway:wght@500;600&family=Playfair+Display:wght@400&display=swap">
<style>
  :root {
    --ink: #000000;
    --paper: #ffffff;
    --photo-light: #d9d9d9;
    --photo-mid: #6e6e6e;
    --photo-dark: #141414;
  }
  html, body {
    margin: 0;
    padding: 0;
    background: var(--ink);
    overflow: hidden;
  }
  .poster {
    position: relative;
    width: 960px;
    height: 1200px;
    background: var(--ink);
    color: var(--paper);
    overflow: hidden;
  }
  .poster > * {
    position: absolute;
    left: 0;
    width: 100%;
    margin: 0;
    text-align: center;
    line-height: 1;
  }
  .recital-label {
    top: 74px;
    font-family: "Raleway", sans-serif;
    font-weight: 600;
    font-size: 27px;
    letter-spacing: 7.6px;
    text-transform: uppercase;
  }
  .hero-photo {
    top: 0;
    height: 1200px;
  }
  .event-date {
    top: 478px;
  }
  .event-date span { display: block; }
  .date-day {
    font-family: "Playfair Display", serif;
    font-size: 34px;
  }
  .date-month {
    margin-top: 8px;
    font-family: "Oswald", sans-serif;
    font-weight: 400;
    font-size: 28px;
    letter-spacing: 4px;
  }
  .date-year {
    margin-top: 2px;
    font-family: "Oswald", sans-serif;
    font-weight: 500;
    font-size: 42px;
    letter-spacing: 6px;
  }
  .recital-title {
    top: 858px;
    font-family: "Oswald", sans-serif;
    font-weight: 400;
    font-size: 118px;
    letter-spacing: 30px;
    padding-left: 30px;
    box-sizing: border-box;
  }
  .recital-subtitle {
    top: 978px;
    font-family: "Oswald", sans-serif;
    font-weight: 300;
    font-size: 62px;
    letter-spacing: 3.2px;
    transform: scaleX(0.86);
  }
  .venue {
    top: 1108px;
    font-family: "Raleway", sans-serif;
    font-weight: 600;
    font-size: 25px;
    letter-spacing: 6px;
    line-height: 1.4;
  }
</style>
</head>
<body>
  <main class="poster">
    <p class="recital-label">Dario Venturelli Senior Saxophone Recital</p>

    <svg class="hero-photo" width="960" height="1200" viewBox="0 0 960 1200" role="img"
         aria-label="Black and white photograph of legs walking down a dim corridor toward bright light, cropped into a triangle">
      <defs>
        <linearGradient id="photo-tone" x1="0" y1="0" x2="0" y2="1">
          <stop offset="0" stop-color="var(--photo-dark)"/>
          <stop offset="0.3" stop-color="var(--photo-mid)"/>
          <stop offset="0.55" stop-color="var(--photo-light)" stop-opacity="0.75"/>
          <stop offset="0.72" stop-color="var(--photo-mid)"/>
          <stop offset="0.78" stop-color="var(--photo-dark)"/>
          <stop offset="1" stop-color="#262626"/>
        </linearGradient>
        <linearGradient id="photo-shade" x1="0" y1="0" x2="1" y2="0">
          <stop offset="0" stop-color="#000" stop-opacity="0.1"/>
          <stop offset="0.5" stop-color="#000" stop-opacity="0.55"/>
          <stop offset="1" stop-color="#000" stop-opacity="0.35"/>
        </linearGradient>
      </defs>
      <polygon points="466,158 845,785 100,785" fill="url(#photo-tone)"/>
      <polygon points="466,158 845,785 100,785" fill="url(#photo-shade)"/>
    </svg>

    <p class="event-date">
      <span class="date-day">8</span>
      <span class="date-month">DECEMBER</span>
      <span class="date-year">2013</span>
    </p>

    <h1 class="recital-title">QUILL</h1>
    <h2 class="recital-subtitle">A VOYAGE BENEATH THE EDGE OF TONE</h2>

    <p class="venue">ALDEN R. MARSH<br>RECITAL HALL</p>
  </main>
</body>
</html>
```